Startup internet service provider needs a good facebook ad

Looking for a catchy facebook ad to launch our internet service in Parker, Colorado. Short video or slideshow preferred, still pictures are okay.

https://www.facebook.com/BrimcoreNetworks

www.brimcore-networks.example

Target Market(s)

Parker Colorado

Colors
add136
0255a3

```html
<!DOCTYPE html>
<html lang="en">
<head>
<meta charset="utf-8">
<title>Brimcore Networks – Fast and Reliable Internet</title>
<link rel="stylesheet" href="https://fonts.googleapis.com/css2?family=Plus+Jakarta+Sans:wght@700;800&family=Inter:wght@400;500&display=swap">
<style>
  :root {
    --lime: #add136;
    --brand-blue: #0255a3;
    --navy: #061f6e;
    --deep: #0a2a8c;
    --glow: #36c8f0;
    --ink: #0f2a4a;
    --white: #ffffff;
  }
  * { margin: 0; padding: 0; box-sizing: border-box; }
  html, body { width: 1200px; height: 1000px; overflow: hidden; background: var(--white); }
  .canvas { position: relative; width: 1200px; height: 1000px; background: var(--white); }

  .ad-banner {
    position: absolute; left: 42px; top: 208px; width: 1116px; height: 584px;
    overflow: hidden;
    background: linear-gradient(100deg, var(--navy) 0%, var(--deep) 45%, #0b3aa8 100%);
  }
  .ad-backdrop { position: absolute; inset: 0; width: 100%; height: 100%; }

  .headline {
    position: absolute; left: 75px; top: 100px;
    font-family: "Plus Jakarta Sans", sans-serif; font-weight: 800;
    font-size: 58px; line-height: 64px; letter-spacing: -0.5px; color: var(--white);
  }
  .subline {
    position: absolute; left: 75px; top: 248px;
    font-family: "Plus Jakarta Sans", sans-serif; font-weight: 700;
    font-size: 32px; line-height: 46px; letter-spacing: -0.3px; color: var(--white);
  }
  .cta-order {
    position: absolute; left: 74px; top: 414px; width: 192px; height: 63px;
    border-radius: 32px; background: var(--lime);
    box-shadow: 0 10px 28px rgba(173, 209, 54, 0.45);
    display: flex; align-items: center; justify-content: center;
    font-family: "Plus Jakarta Sans", sans-serif; font-weight: 800; font-size: 16px;
    color: var(--ink); letter-spacing: 0.1px;
  }
  .contact-row {
    position: absolute; left: 86px; top: 516px;
    display: flex; align-items: center; gap: 70px;
    font-family: "Inter", sans-serif; font-size: 22px; color: var(--white);
  }
  .contact-item { display: flex; align-items: center; gap: 14px; }
  .contact-icon { width: 24px; height: 24px; flex: none; }

  .brand-plate {
    position: absolute; left: 673px; top: 168px; width: 367px; height: 79px;
    background: var(--white); border-radius: 6px;
    display: flex; align-items: center; gap: 14px; padding-left: 18px;
  }
  .brand-dot { width: 42px; height: 42px; border-radius: 50%; background: var(--brand-blue); flex: none; }
  .brand-name {
    font-family: "Plus Jakarta Sans", sans-serif; font-weight: 700;
    font-size: 26px; color: var(--brand-blue); letter-spacing: -0.2px;
  }
</style>
</head>
<body>
<div class="canvas">
  <section class="ad-banner">
    <svg class="ad-backdrop" viewBox="0 0 1116 584" preserveAspectRatio="none">
      <defs>
        <radialGradient id="fiberGlow" cx="0.55" cy="0.35" r="0.7">
          <stop offset="0" stop-color="#3fd6ff"/>
          <stop offset="0.35" stop-color="#1a8fe6"/>
          <stop offset="0.7" stop-color="#0c3fa8"/>
          <stop offset="1" stop-color="#0a1a3a"/>
        </radialGradient>
        <radialGradient id="lowerBokeh" cx="0.75" cy="0.9" r="0.6">
          <stop offset="0" stop-color="#1f6fe0" stop-opacity="0.7"/>
          <stop offset="1" stop-color="#1f6fe0" stop-opacity="0"/>
        </radialGradient>
      </defs>
      <rect x="0" y="0" width="1116" height="584" fill="url(#lowerBokeh)"/>
      <polygon points="390,0 1116,0 1116,432 693,432" fill="url(#fiberGlow)"
               role="img" aria-label="Glowing blue fibre-optic strands photograph"/>
      <polygon points="390,0 416,0 716,432 1116,432 1116,449 693,449"
               fill="#3aa6f2" opacity="0.75"/>
    </svg>

    <h1 class="headline">Fast and<br>Reliable</h1>
    <p class="subline">internet service designed<br>and catered to meet<br>your needs</p>
    <div class="cta-order">ORDER SERVICE</div>

    <div class="contact-row">
      <span class="contact-item">
        <svg class="contact-icon" viewBox="0 0 24 24"><path fill="#add136" d="M6.6 10.8a15.2 15.2 0 0 0 6.6 6.6l2.2-2.2c.3-.3.7-.4 1-.2 1.1.4 2.3.6 3.6.6.6 0 1 .4 1 1V20c0 .6-.4 1-1 1A17 17 0 0 1 3 4c0-.6.4-1 1-1h3.5c.6 0 1 .4 1 1 0 1.3.2 2.5.6 3.6.1.3 0 .7-.2 1z"/></svg>
        844-555-0137
      </span>
      <span class="contact-item">
        <svg class="contact-icon" viewBox="0 0 24 24"><rect x="1" y="4" width="22" height="16" rx="1.5" fill="#add136"/><path d="M2 5l10 7.5L22 5" fill="none" stroke="#0a2a8c" stroke-width="1.6"/></svg>
        information@brimcore-networks.example
      </span>
    </div>

    <div class="brand-plate">
      <span class="brand-dot"></span>
      <span class="brand-name">Brimcore Networks</span>
    </div>
  </section>
</div>
</body>
</html>
```